LinkedIn Ad Image Design Competition

We're seeking creative designers to develop a series of engaging LinkedIn advertisements for Tidelark with original art work.

The goal is to create scroll-stopping ads that capture attention through humor, nostalgia, and compelling storytelling while maintaining professional appeal.

Creative Brief:
Please read the "Core Messages to Convey"
https://notes.quillharbor.net/page/d/7kwtrVbQ3MeHxnLsYpRCuA52-h08tjzNG_e61mqaLp4/view?tab=t.0#section=h.4rkdwmqhz2c

Target Market(s)

Busy executives focusing on making their company more efficient

Requirements
Must have
• An image ( not copy) that speaks to one of our "Core Messages to Convey"

```html
<!DOCTYPE html>
<html lang="en">
<head>
<meta charset="utf-8">
<title>Tidelark LinkedIn Ad Series</title>
<link href="https://fonts.googleapis.com/css2?family=Montserrat:wght@400;600;700;800&family=Oswald:wght@500&family=Open+Sans:wght@400;600;700&display=swap" rel="stylesheet">
<style>
:root{
  --board:#e3e3e3;
  --ink:#111;
  --teal-dark:#165f72;
  --teal:#3fa3b7;
  --teal-band:rgba(52,150,170,.82);
  --gold:#f2b51e;
  --amber:#f6c744;
  --orange:#f26a21;
  --white:#fff;
  --slate:#2c4554;
}
*{margin:0;padding:0;box-sizing:border-box}
html,body{width:1200px;height:434px;overflow:hidden;background:var(--white)}
body{position:relative;font-family:"Montserrat",sans-serif;color:var(--ink)}
.board{position:absolute;left:31px;top:21px;width:1137px;height:357px;background:var(--board);box-shadow:0 4px 6px rgba(0,0,0,.25)}
.ad{position:absolute;overflow:hidden}
.photo{position:absolute;inset:0}
.brand{display:flex;align-items:center;gap:3px;font-family:"Montserrat",sans-serif;font-weight:600}
.brand i{display:block;border-radius:50%;background:currentColor}
/* hero ad */
.hero{left:49px;top:30px;width:324px;height:323px;background:var(--white)}
.hero .photo{top:40px;bottom:46px;background:linear-gradient(180deg,#e8eef0 0%,#9fb3bd 35%,#5d7584 70%,#3c5866 100%)}
.hero .kicker{position:absolute;left:14px;top:14px;font-size:12.5px;font-weight:700;color:var(--slate)}
.hero .title{position:absolute;left:13px;top:27px;font-size:27px;font-weight:800;color:var(--teal-dark);line-height:1}
.hero .sub{position:absolute;left:14px;top:54px;font-size:12.5px;font-weight:800;color:var(--teal-dark)}
.hero .ribbon{position:absolute;left:217px;top:0;width:93px;height:100px}
.hero .ribbon-text{position:absolute;left:217px;top:18px;width:93px;text-align:center;color:var(--white);font-family:"Open Sans",sans-serif}
.hero .ribbon-text b{display:block;font-size:23px;font-weight:600;line-height:1.1}
.hero .ribbon-text span{display:block;font-size:9.5px;font-weight:600;line-height:1.25}
.hero .band{position:absolute;left:0;right:0;top:180px;height:97px;background:var(--teal-band)}
.hero .band h3{position:absolute;left:17px;top:5px;font-family:"Open Sans",sans-serif;font-size:13px;font-weight:600;color:var(--white);line-height:1.2}
.hero .band p{position:absolute;left:17px;right:4px;top:35px;font-family:"Open Sans",sans-serif;font-size:4.6px;line-height:1.38;color:var(--amber)}
.hero .foot{position:absolute;left:14px;top:288px;color:var(--teal-dark);font-weight:700}
.hero .foot small{display:block;font-size:9px}
.hero .foot strong{display:block;font-size:13px;font-weight:800}
.hero .brand{position:absolute;right:14px;top:300px;font-size:11px;color:var(--teal)}
.hero .brand i{width:8px;height:8px}
/* tiles */
.tile{width:100px;height:100px;text-align:center;color:var(--white)}
.tile .copy{position:absolute;left:4px;right:4px;top:6px;line-height:1.1}
.tile .foot{position:absolute;left:4px;bottom:4px;text-align:left;font-size:3px;font-weight:700;line-height:1.2}
.tile .foot b{display:block;font-size:4.2px}
.tile .brand{position:absolute;right:4px;bottom:4px;font-size:3.6px}
.tile .brand i{width:3px;height:3px}
.lg{font-size:9px;font-weight:800}
.md{font-size:6.5px;font-weight:700}
.sm{font-size:3.6px;font-weight:600}
.xs{font-size:2.4px;line-height:1.3}
.tag{position:absolute;right:0;top:0;width:32px;height:30px;clip-path:polygon(0 0,100% 0,100% 100%,50% 82%,0 100%)}
.tag span{display:block;font-size:7px;font-weight:800;padding-top:6px;line-height:1}
.tag small{display:block;font-size:2.2px}
.c1{left:389px}.c2{left:496px}.c3{left:603px}.c4{left:709px}
.r1{top:30px}.r2{top:142px}.r3{top:253px}
/* closing ad */
.close{left:827px;top:30px;width:324px;height:323px;text-align:center}
.close .photo{background:linear-gradient(180deg,#d7b2ad 0%,#c98f86 25%,#8e7b80 50%,#6d7379 72%,#b9bcbd 100%)}
.close h2{position:absolute;left:0;right:0;font-weight:800;line-height:1}
.close .l1{top:36px;font-size:23px;color:var(--ink)}
.close .l2{top:62px;font-size:31px;color:var(--white)}
.close .l3{top:126px;font-size:20px;font-weight:700;color:var(--ink)}
.close .l4{top:154px;font-family:"Open Sans",sans-serif;font-size:31px;font-weight:700;color:var(--white)}
.close .l5{top:192px;font-family:"Open Sans",sans-serif;font-size:31px;font-weight:700;color:var(--white)}
.close .brand{position:absolute;left:88px;top:283px;font-size:21px;color:var(--orange);gap:6px}
.close .brand i{width:16px;height:16px}
.caption{position:absolute;left:0;right:0;top:390px;text-align:center;font-family:"Open Sans",sans-serif;font-size:23px;font-weight:600;color:var(--ink)}
</style>
</head>
<body>
<main class="board" aria-label="Ad series presentation"></main>

<section class="ad hero">
  <div class="photo" role="img" aria-label="City skyline with tall towers and a reflective sculpture"></div>
  <p class="kicker">THE TRUE COST OF</p>
  <h1 class="title">DATA SILOS &amp;</h1>
  <p class="sub">SYSTEM FRAGMENTATION</p>
  <svg class="ribbon" viewBox="0 0 93 100" aria-hidden="true"><polygon points="0,0 93,0 93,100 46.5,78 0,100" fill="#4aa6b8"/></svg>
  <div class="ribbon-text"><b>Let's</b><span>Streamline Your</span><span>Disparate Data</span></div>
  <div class="band">
    <h3>Attending the Operating<br>Partners Forum?</h3>
    <p>In the aftermath of mergers and acquisitions, organizations find themselves grappling with a complex web of disparate systems and isolated data repositories. While the challenges of integration are often acknowledged, the true cost of persistent data silos and system fragmentation is frequently underestimated. This section delves into the multifaceted impact of these issues, exploring both the obvious inefficiencies and the less visible, yet equally damaging, consequences for merged organizations. The true cost of data silos and system fragmentation extends far beyond the immediately visible inefficiencies. From missed revenue opportunities and increased operational costs to more subtle erosion of innovation potential and talent retention, these issues permeate every aspect of organizational performance. Recognizing and quantifying these diverse impacts is the first step toward developing a comprehensive strategy for post-M&amp;A system integration - a strategy that not only mitigates these costs but transforms integration challenges into drivers of value creation.</p>
  </div>
  <div class="foot"><small>DATA CONSULTANCY FOR</small><strong>PRIVATE EQUITY AND M&amp;A</strong></div>
  <div class="brand"><i></i>tidelark</div>
</section>

<!-- row 1 -->
<section class="ad tile c1 r1" style="background:#fff">
  <div class="photo" role="img" aria-label="City skyline at dusk" style="top:32px;bottom:16px;background:linear-gradient(180deg,#7aa7d6,#2f4f80 60%,#1d2d4a)"></div>
  <div class="copy" style="text-align:left;color:#1f6fb3"><div class="sm" style="color:#222">THE TRUE COST OF</div><div class="md" style="font-weight:800">DATA SILOS &amp;</div><div class="sm">SYSTEM FRAGMENTATION</div></div>
  <div class="tag" style="background:#2f86c6"><span>GET</span><small>FREE VALUE CREATION PLAYBOOK</small></div>
  <div class="copy" style="top:52px;text-align:left"><div class="sm">Attending the Harbrook Operating Partners Forum?</div><div class="xs">Fragmented systems quietly drain value after every deal closes. Learn where it leaks.</div></div>
  <div class="foot" style="color:#1f6fb3;background:#fff;left:0;right:0;padding:2px 4px;bottom:0">DATA CONSULTANCY FOR<b>PRIVATE EQUITY AND M&amp;A</b></div>
  <div class="brand" style="color:#1f6fb3">tidelark</div>
</section>
<section class="ad tile c2 r1" style="background:#1c2430">
  <div class="photo" role="img" aria-label="City skyline at night" style="background:linear-gradient(180deg,#1a1f28,#2c3a4c 60%,#1b2028)"></div>
  <div class="copy" style="text-align:left"><div class="xs" style="font-size:3.2px">OVERCOMING TECHNICAL</div><div class="md" style="color:var(--gold);font-weight:800">CHALLENGES</div><div class="sm" style="color:var(--gold)">IN SYSTEM UNIFICATION</div></div>
  <div class="tag" style="background:var(--gold);color:#222"><span>GET</span><small>FREE VALUE CREATION PLAYBOOK</small></div>
  <div class="copy" style="top:52px;text-align:left"><div class="sm">Now That You're Back From The Harbrook Operating Partners Conference</div><div class="xs">Turn new ideas into a clear plan for unifying portfolio systems and data.</div></div>
  <div class="foot">DATA CONSULTANCY FOR<b>PRIVATE EQUITY AND M&amp;A</b></div>
  <div class="brand" style="color:var(--gold)">tidelark</div>
</section>
<section class="ad tile c3 r1">
  <div class="photo" role="img" aria-label="Robotic arm in a bright workspace" style="background:linear-gradient(180deg,#dfe6ea,#b3c2cb 60%,#8fa2ad)"></div>
  <div class="tag" style="left:4px;right:auto;background:rgba(255,255,255,.4)"><span>GET</span><small>FREE VALUE CREATION PLAYBOOK</small></div>
  <div class="copy" style="left:40px;top:12px;text-align:left;color:#222"><div class="sm">ATTENDING OPERATING PARTNERS NY?</div></div>
  <div class="copy" style="top:38px;text-align:left"><div class="lg" style="font-size:12px">UNLOCKING</div><div class="md" style="font-size:8px">POST-M&amp;A VALUE</div><div class="xs">A Blueprint for Conquering Data Silos and System Fragmentation</div></div>
  <div class="foot" style="color:#222;bottom:12px">DATA CONSULTANCY FOR<b>PRIVATE EQUITY AND M&amp;A</b></div>
  <div class="brand" style="color:#222;left:4px;right:auto">tidelark</div>
</section>
<section class="ad tile c4 r1">
  <div class="photo" role="img" aria-label="Misty autumn landscape" style="background:linear-gradient(180deg,#b7c6cf,#dfe4e6 50%,#aab8bf)"></div>
  <div class="copy"><div class="md" style="font-size:9px">WHAT WOULD<br>YOU RATHER DO?</div></div>
  <div class="copy" style="top:36px;color:#222"><div class="lg" style="font-size:11px">CRUNCH</div><div class="xs" style="font-size:3px">NUMBERS ALL AUTUMN</div><div class="md">Or</div><div class="lg" style="font-size:11px">CRUNCH</div><div class="xs" style="font-size:3px">THROUGH AUTUMN LEAVES</div></div>
  <div class="foot">DATA CONSULTANCY FOR<b>PRIVATE EQUITY AND M&amp;A</b></div>
  <div class="brand" style="color:#222">tidelark</div>
</section>

<!-- row 2 -->
<section class="ad tile c1 r2">
  <div class="photo" role="img" aria-label="Corn maze under a pale sky" style="background:linear-gradient(180deg,#f2c7b8,#e6d9cf 45%,#b9b2a4)"></div>
  <div class="copy"><div class="md" style="font-size:9px">WHAT WOULD<br>YOU RATHER DO?</div></div>
  <div class="copy" style="top:36px;color:#222"><div class="md" style="letter-spacing:1px">GET LOST IN</div><div class="lg" style="font-size:10px">DATA SILOS</div><div class="xs">or</div><div class="md" style="letter-spacing:1px">GET LOST IN A</div><div class="lg" style="font-size:10px">CORN MAZE</div></div>
  <div class="foot" style="color:#222">DATA CONSULTANCY FOR<b>PRIVATE EQUITY AND M&amp;A</b></div>
  <div class="brand" style="color:#222">tidelark</div>
</section>
<section class="ad tile c2 r2">
  <div class="photo" role="img" aria-label="Autumn trees by a lake" style="background:linear-gradient(180deg,#8ea0ad,#6f7a70 50%,#3b4034)"></div>
  <div class="copy"><div class="md" style="font-size:9px">WHAT WOULD<br>YOU RATHER DO?</div></div>
  <div class="copy" style="top:38px;color:var(--amber)"><div class="md" style="letter-spacing:1px">RAKE THROUGH</div><div class="lg" style="font-size:11px">MESSY DATA</div><div class="xs">or</div><div class="sm" style="letter-spacing:.5px">ENJOY THE FALLING LEAVES</div></div>
  <div class="foot">DATA CONSULTANCY FOR<b>PRIVATE EQUITY AND M&amp;A</b></div>
  <div class="brand">tidelark</div>
</section>
<section class="ad tile c3 r2">
  <div class="photo" role="img" aria-label="Coastal road by the sea" style="background:linear-gradient(180deg,#eef1f2,#9bb4c3 45%,#4e6b7e 75%,#3a4a52)"></div>
  <div class="copy" style="top:10px;color:#222"><div class="sm" style="font-size:5px">HOW'S YOUR TIME</div><div class="lg">BETTER SPENT?</div></div>
  <div class="copy" style="top:40px;color:var(--gold)"><div class="xs" style="font-size:3px">TRYING TO MAKE SENSE OF YOUR</div><div class="md" style="font-size:7.5px">DISPARATE DATA</div><div class="xs">or</div><div class="xs" style="font-size:3px">MAKING MEMORIES WITH</div><div class="md" style="font-size:8px">YOUR FAMILY</div></div>
  <div class="foot">DATA CONSULTANCY FOR<b>PRIVATE EQUITY AND M&amp;A</b></div>
  <div class="brand">tidelark</div>
</section>
<section class="ad tile c4 r2">
  <div class="photo" role="img" aria-label="Family walking into an orange sunset" style="background:linear-gradient(180deg,#f07a3a,#f6a04a 45%,#6b3a22 85%)"></div>
  <div class="copy" style="top:9px;color:#1a1a1a;font-family:'Oswald',sans-serif"><div style="font-size:6.5px">SPEND TIME WITH YOUR FAMILY</div><div style="font-size:4px;letter-spacing:.3px">NOT CONSOLIDATING YOUR DATA</div></div>
  <div class="foot">DATA CONSULTANCY FOR<b>PRIVATE EQUITY AND M&amp;A</b></div>
  <div class="brand">tidelark</div>
</section>

<!-- row 3 -->
<section class="ad tile c1 r3">
  <div class="photo" role="img" aria-label="Calm turquoise sea" style="background:linear-gradient(180deg,#8fd3c8,#bfe3d9 45%,#7cb8ad)"></div>
  <div class="copy" style="top:12px"><div class="sm" style="font-size:5.5px">POST-MERGER DATA</div><div class="md" style="color:var(--orange);font-size:8px">CONSOLIDATION</div><div class="xs" style="color:var(--orange);font-size:3.6px">FOR PRIVATE EQUITY AND M&amp;A</div></div>
  <div class="copy" style="top:50px"><div class="xs" style="font-size:3px">Don't Let Portcos Build A Tower Of Babel</div><div class="md">It's Not A Good Look</div></div>
  <div class="foot">DATA CONSULTANCY FOR<b>PRIVATE EQUITY AND M&amp;A</b></div>
  <div class="brand">tidelark</div>
</section>
<section class="ad tile c2 r3">
  <div class="photo" role="img" aria-label="Lone bare tree in fog" style="background:linear-gradient(180deg,#d8d2c4,#a8a290 50%,#4a4436)"></div>
  <div class="copy" style="top:12px;color:#222"><div class="sm" style="font-size:5.5px">POST-MERGER DATA</div><div class="md" style="font-size:8px">CONSOLIDATION</div><div class="xs" style="font-size:3.6px">FOR PRIVATE EQUITY AND M&amp;A</div></div>
  <div class="copy" style="top:50px;color:var(--orange)"><div class="xs">Grow your portfolio with</div><div class="lg" style="font-size:11px">Bolt-ons</div><div class="xs">without a tower of Babel</div></div>
  <div class="foot" style="color:var(--orange)">DATA CONSULTANCY FOR<b>PRIVATE EQUITY AND M&amp;A</b></div>
  <div class="brand" style="color:var(--orange)">tidelark</div>
</section>
<section class="ad tile c3 r3">
  <div class="photo" role="img" aria-label="Sea of clouds under a blue sky" style="background:linear-gradient(180deg,#b7cdd9,#e3e8ea 55%,#c9d3d8)"></div>
  <div class="copy" style="top:12px;color:#26343d"><div class="sm" style="font-size:5.5px">POST-MERGER DATA</div><div class="md" style="font-size:8px">CONSOLIDATION</div><div class="xs" style="font-size:3.6px">FOR PRIVATE EQUITY AND M&amp;A</div></div>
  <div class="copy" style="top:48px;color:#26343d"><div class="lg" style="font-size:11px">"Bolt-on"</div><div class="xs" style="font-size:3px">is not supposed to be a literal term</div></div>
  <div class="foot" style="color:#26343d">DATA CONSULTANCY FOR<b>PRIVATE EQUITY AND M&amp;A</b></div>
  <div class="brand" style="color:#26343d">tidelark</div>
</section>
<section class="ad tile c4 r3">
  <div class="photo" role="img" aria-label="Frosted winter forest at pink dawn" style="background:linear-gradient(180deg,#f2b9a6,#e7cfd0 45%,#9a9ec8)"></div>
  <div class="copy" style="top:12px;color:#26343d"><div class="sm" style="font-size:5.5px">POST-MERGER DATA</div><div class="md" style="font-size:8px">CONSOLIDATION</div><div class="xs" style="font-size:3.6px">FOR PRIVATE EQUITY AND M&amp;A</div></div>
  <div class="copy" style="top:42px;color:#1a1a1a"><div class="xs" style="font-size:2.8px">How do you merge multiple ERPs?</div><div class="xs">Hint:</div><div class="lg" style="font-size:10px">"Pivotra"</div><div class="xs" style="font-size:3px">is not a valid answer</div></div>
  <div class="foot">DATA CONSULTANCY FOR<b>PRIVATE EQUITY AND M&amp;A</b></div>
  <div class="brand">tidelark</div>
</section>

<section class="ad close">
  <div class="photo" role="img" aria-label="Sky above pink sunset clouds"></div>
  <h2 class="l1">POST-MERGER ERP</h2>
  <h2 class="l2">CONSOLIDATION</h2>
  <h2 class="l3">for</h2>
  <h2 class="l4">Private Equity &amp;</h2>
  <h2 class="l5">M&amp;A</h2>
  <div class="brand"><i></i>tidelark</div>
</section>

<p class="caption">Images Not Included In Design</p>
</body>
</html>
```